Brookside Grocer

Hope all is well!

Wanted to make business cards for my father. His name is Faisal Qureshi and owns convenience stores. I have attached logo :)

He does not want any title just simple name and phone. An email would be nice as well.

Faisal Qureshi
Cell: 413-585-2046
Store: 413-719-4820

Brooksidegrocer512@fernpost.com

The design and style is totally up to you :) The colors we were looking for were the same as logo :)

```html
<!DOCTYPE html>
<html lang="en">
<head>
<meta charset="utf-8">
<title>Brookside Grocer – Business Cards</title>
<link rel="stylesheet" href="https://fonts.googleapis.com/css2?family=Libre+Baskerville:wght@700&family=Arimo:wght@400&display=swap">
<style>
  :root {
    --backdrop: #e4e4e2;
    --card-navy: #243776;
    --accent-red: #e8343a;
    --ink-white: #ffffff;
    --rule-grey: #9aa3c4;
    --disc-blue: #4f68b8;
  }
  * { box-sizing: border-box; margin: 0; padding: 0; }
  html, body { width: 1200px; height: 802px; overflow: hidden; }
  body {
    background: var(--backdrop);
    position: relative;
    font-family: "Arimo", Arial, sans-serif;
  }
  .card {
    position: absolute;
    top: 258px;
    width: 500px;
    height: 286px;
    background: var(--card-navy);
    border-bottom: 3px solid var(--accent-red);
    border-left: 3px solid var(--accent-red);
    overflow: hidden;
    box-shadow: 0 14px 30px rgba(0,0,0,.18);
  }
  .card--front { left: 70px; }
  .card--back { left: 630px; }

  .brand-name {
    font-family: "Libre Baskerville", Georgia, serif;
    font-weight: 700;
    color: var(--ink-white);
    line-height: 1.1;
    text-transform: uppercase;
    letter-spacing: .5px;
  }
  .card--front .brand-name {
    position: absolute;
    left: 40px;
    top: 118px;
    width: 170px;
    font-size: 24px;
  }
  .divider {
    position: absolute;
    left: 228px;
    top: 88px;
    width: 1px;
    height: 110px;
    background: var(--rule-grey);
  }
  .contact {
    position: absolute;
    left: 250px;
    top: 86px;
    color: var(--ink-white);
  }
  .person-name {
    font-family: "Libre Baskerville", Georgia, serif;
    font-weight: 700;
    font-size: 17px;
    text-transform: uppercase;
    margin-bottom: 14px;
  }
  .person-name .surname { color: var(--accent-red); }
  .contact-line {
    display: flex;
    align-items: center;
    gap: 8px;
    font-size: 12.5px;
    line-height: 1;
    margin-bottom: 9px;
  }
  .contact-line svg { width: 12px; height: 12px; flex: none; }

  .disc {
    position: absolute;
    left: -30px;
    top: 60px;
    width: 300px;
    height: 300px;
    border-radius: 50%;
    background: radial-gradient(circle at 65% 40%, var(--disc-blue), #3a4f9c 70%);
    box-shadow: inset 0 0 0 1px rgba(255,255,255,.15);
  }
  .card--back .brand-name {
    position: absolute;
    right: 30px;
    top: 118px;
    font-size: 30px;
    text-align: right;
  }
</style>
</head>
<body>
  <section class="card card--front" aria-label="Business card front">
    <div class="brand-name">Brookside Grocer</div>
    <div class="divider"></div>
    <div class="contact">
      <p class="person-name">Faisal <span class="surname">Qureshi</span></p>
      <p class="contact-line">
        <svg viewBox="0 0 12 12" aria-hidden="true"><rect x="3" y="1" width="6" height="10" rx="1" fill="none" stroke="#e8343a" stroke-width="1.4"/></svg>
        413-585-2046
      </p>
      <p class="contact-line">
        <svg viewBox="0 0 12 12" aria-hidden="true"><path d="M2 2c0 5 3 8 8 8l1-2-2.5-1.5-1 1C6 7 5 6 4.5 4.5l1-1L4 1z" fill="#e8343a"/></svg>
        413-719-4820
      </p>
      <p class="contact-line">
        <svg viewBox="0 0 12 12" aria-hidden="true"><rect x="1" y="2.5" width="10" height="7" fill="none" stroke="#e8343a" stroke-width="1.2"/><path d="M1 2.5l5 4 5-4" fill="none" stroke="#e8343a" stroke-width="1.2"/></svg>
        Brooksidegrocer512@fernpost.com
      </p>
    </div>
  </section>

  <section class="card card--back" aria-label="Business card back">
    <div class="disc" role="img" aria-label="Large pressed emblem area"></div>
    <div class="brand-name">Brookside<br>Grocer</div>
  </section>
</body>
</html>
```